Business Card for a Wedding Films Business

We require a business card design for our business 'Lewis Barnow Wedding Films'. The logo needs to look classy and high end.

Target Market(s)

Wedding Couples

Contact Information for Business Card

Lewis Barnow Wedding Films
07312 580 417
films@lewisbarnow-example.com
www.lewisbarnow-example.com

Facebook: @lewisbarnowweddingfilms
Instagram: @lewisbarnowfilms

Font styles to use
Sans Serif

Requirements
Must have
• Social media icons - Facebook and Instagram

```html
<!DOCTYPE html>
<html lang="en">
<head>
<meta charset="utf-8">
<title>Lewis Barnow Wedding Films – Business Card</title>
<link rel="stylesheet" href="https://fonts.googleapis.com/css2?family=Jost:wght@500;600&family=Arimo:wght@400&display=swap">
<style>
  :root {
    --backdrop: #1c1c1c;
    --kraft-light: #dfbf92;
    --kraft-mid: #c9a171;
    --kraft-dark: #a87a4c;
    --ink: #111010;
  }
  * { margin: 0; padding: 0; box-sizing: border-box; }
  html, body {
    width: 1093px; height: 1200px; overflow: hidden;
    background: var(--backdrop);
  }
  .canvas { position: relative; width: 1093px; height: 1200px; }

  .card {
    position: absolute; left: 264px; width: 580px; height: 357px;
    background: radial-gradient(ellipse at 30% 0%, var(--kraft-light) 0%, var(--kraft-mid) 55%, var(--kraft-dark) 100%);
    color: var(--ink);
    text-align: center;
  }
  .card--front { top: 226px; }
  .card--back { top: 620px; }

  .brand { position: absolute; left: 0; right: 0; }
  .brand__name {
    font-family: "Jost", sans-serif; font-weight: 600;
    font-size: 29px; letter-spacing: 9px; line-height: 1;
    text-transform: uppercase; padding-left: 9px;
  }
  .brand__tagline {
    font-family: "Jost", sans-serif; font-weight: 600;
    font-size: 14px; letter-spacing: 9.5px; line-height: 1;
    text-transform: uppercase; padding-left: 9.5px; margin-top: 9px;
  }
  .card--front .brand { top: 56px; }
  .card--back .brand { top: 203px; }

  .divider {
    position: absolute; left: 0; right: 0;
    display: flex; justify-content: center; align-items: center; gap: 5px;
  }
  .divider__rule { width: 33px; height: 1px; background: var(--ink); margin: 0 3px; }
  .divider--contact { top: 125px; }
  .divider--social { top: 242px; }
  .divider--social .divider__rule { width: 50px; }

  .icon-tile {
    width: 24px; height: 24px; border-radius: 3px; background: var(--ink);
    display: flex; align-items: center; justify-content: center;
  }
  .icon-tile svg { width: 16px; height: 16px; }
  .plain-mark { width: 22px; height: 22px; background: var(--ink); border-radius: 2px; }
  .plain-mark--round { background: none; border: 2.5px solid var(--ink); border-radius: 50%; }

  .details {
    position: absolute; left: 0; right: 0;
    font-family: "Arimo", sans-serif; font-size: 17px; line-height: 21px;
  }
  .details--contact { top: 162px; }
  .details--social { top: 277px; }
</style>
</head>
<body>
<main class="canvas">
  <section class="card card--front">
    <div class="brand">
      <div class="brand__name">Lewis Barnow</div>
      <div class="brand__tagline">Wedding Films</div>
    </div>

    <div class="divider divider--contact">
      <span class="divider__rule"></span>
      <span class="icon-tile" aria-label="Phone">
        <svg viewBox="0 0 16 16" fill="var(--kraft-mid)"><path d="M2 6c0-2 3-3 6-3s6 1 6 3v1h-3V6H5v1H2z"/><path d="M4 8h8l1 5H3z"/></svg>
      </span>
      <span class="icon-tile" aria-label="Email">
        <svg viewBox="0 0 16 16" fill="none" stroke="var(--kraft-mid)" stroke-width="1.3"><rect x="1.5" y="3.5" width="13" height="9"/><path d="M1.5 3.5 8 9l6.5-5.5M1.5 12.5 6 8m8.5 4.5L10 8"/></svg>
      </span>
      <span class="icon-tile" aria-label="Website">
        <svg viewBox="0 0 16 16" fill="none" stroke="var(--kraft-mid)" stroke-width="1.3"><circle cx="8" cy="8" r="6.3"/><path d="M1.7 8h12.6M8 1.7c-3 3.5-3 9 0 12.6M8 1.7c3 3.5 3 9 0 12.6"/></svg>
      </span>
      <span class="divider__rule"></span>
    </div>

    <div class="details details--contact">
      <p>07312 580 417</p>
      <p>films@lewisbarnow-example.com</p>
      <p>www.lewisbarnow-example.com</p>
    </div>

    <div class="divider divider--social" aria-hidden="true">
      <span class="divider__rule"></span>
      <span class="plain-mark"></span>
      <span class="plain-mark plain-mark--round"></span>
      <span class="divider__rule"></span>
    </div>

    <div class="details details--social">
      <p>@lewisbarnowweddingfilms</p>
      <p>@lewisbarnowfilms</p>
    </div>
  </section>

  <section class="card card--back">
    <div class="brand">
      <div class="brand__name">Lewis Barnow</div>
      <div class="brand__tagline">Wedding Films</div>
    </div>
  </section>
</main>
</body>
</html>
```